Business Card and Stationery for Bellwick Home Services
Bellwick Home Services
Professional
R. Owen Tallis
President/CEO
4187 Marrow Creek Lane,
Suite K
Baton Rouge LA 70342
rowentallis@bellwickhomeservices.biz
www.bellwickhomeservice.biz
Commercial License # 53419 Residential LIcense # 21398
The color formula for the orange is:
C=0 M=74 Y=100 K=0
We take care of all of your home needs.
Plumbing, Heating and AIr, Electrical, Remodeling, Roofing, New Construction, Insurance Damage Repairs, Fire Restoration, if its in you home, we can service it or take care of it for you!!!
THESE ARE JUST IDEAS, want to use the back for information, etc.......maybe a light watermark on the back, using part of the logo, showing under the lettering. Would like the back to be the orange color

```html
<!DOCTYPE html>
<html lang="en">
<head>
<meta charset="utf-8">
<title>Bellwick Home Services – Business Card</title>
<link href="https://fonts.googleapis.com/css2?family=Open+Sans:wght@400;600;700&display=swap" rel="stylesheet">
<style>
  :root {
    --orange: #f26522;
    --orange-soft: #f8a173;
    --orange-faint: #fdeee5;
    --ink: #4a4a4a;
    --ink-light: #7a7a7a;
    --paper: #ffffff;
    --backdrop: #e4e4e2;
  }
  * { box-sizing: border-box; margin: 0; padding: 0; }
  html, body {
    width: 1200px; height: 944px; overflow: hidden;
    background: var(--backdrop);
    font-family: "Open Sans", Arial, sans-serif;
  }
  .stage { position: relative; width: 1200px; height: 944px; }

  .card {
    position: absolute;
    width: 760px; height: 434px;
    box-shadow: 0 6px 18px rgba(0,0,0,0.18);
    overflow: hidden;
  }

  /* Back of card */
  .card--back {
    left: 380px; top: 26px;
    background: var(--orange);
    color: var(--paper);
    text-align: center;
    padding-top: 70px;
  }
  .brand {
    display: inline-flex; align-items: center; gap: 14px;
  }
  .brand__mark {
    width: 58px; height: 58px; background: var(--paper);
  }
  .brand__name {
    font-weight: 700; font-size: 40px; letter-spacing: 0.5px;
    color: var(--paper);
  }
  .card--back .tagline {
    margin-top: 34px; font-size: 19px; line-height: 1.5; font-weight: 400;
    padding: 0 60px;
  }

  /* Front of card */
  .card--front {
    left: 60px; top: 486px;
    background: var(--paper);
    color: var(--ink);
  }
  .side-band {
    position: absolute; left: 0; top: 0; bottom: 0; width: 44px;
    background: var(--orange);
  }
  .side-band::after {
    content: ""; position: absolute; right: -12px; top: 0; bottom: 0; width: 4px;
    background: var(--orange-soft);
  }
  .faint-mark {
    position: absolute; right: 90px; top: 120px;
    width: 250px; height: 250px; background: var(--orange-faint);
  }
  .front-content { position: absolute; left: 90px; top: 36px; }
  .card--front .brand__mark { width: 50px; height: 50px; background: var(--orange); }
  .card--front .brand__name { color: var(--orange); font-size: 32px; }
  .licenses {
    margin-top: 20px; font-size: 11px; color: var(--orange); font-weight: 600;
  }
  .licenses span + span { margin-left: 14px; }
  .address { margin-top: 8px; font-size: 14px; line-height: 1.45; }
  .contacts { list-style: none; margin-top: 14px; font-size: 14px; line-height: 1.55; }
  .contacts li { display: flex; align-items: center; gap: 8px; }
  .contacts svg { width: 12px; height: 12px; fill: var(--orange); flex: none; }
  .person {
    position: absolute; right: 56px; bottom: 44px; text-align: left;
  }
  .person__name { font-size: 26px; color: var(--orange); font-weight: 600; }
  .person__title { font-size: 16px; color: var(--ink-light); }
</style>
</head>
<body>
<main class="stage">

  <section class="card card--back" aria-label="Card back">
    <div class="brand">
      <span class="brand__mark"></span>
      <span class="brand__name">Bellwick Home Services</span>
    </div>
    <p class="tagline">We take care of all of your home needs.<br>
      Plumbing, Heating and Air, Electrical, Remodeling, Roofing,<br>
      New Construction, Insurance Damage Repairs, Fire Restoration,<br>
      if it's in your home, we can service it or take care of it for you!</p>
  </section>

  <section class="card card--front" aria-label="Card front">
    <div class="side-band"></div>
    <div class="faint-mark"></div>
    <div class="front-content">
      <div class="brand">
        <span class="brand__mark"></span>
        <span class="brand__name">Bellwick Home Services</span>
      </div>
      <p class="licenses"><span>Commercial License # 53419</span><span>Residential License # 21398</span></p>
      <p class="address">4187 Marrow Creek Lane,<br>Suite K<br>Baton Rouge LA 70342</p>
      <ul class="contacts">
        <li><svg viewBox="0 0 12 12"><circle cx="6" cy="6" r="5"/></svg>225-555-0148</li>
        <li><svg viewBox="0 0 12 12"><circle cx="6" cy="6" r="5"/></svg>225-555-0193</li>
        <li><svg viewBox="0 0 12 12"><circle cx="6" cy="6" r="5"/></svg>504-555-0162</li>
        <li><svg viewBox="0 0 12 12"><circle cx="6" cy="6" r="5"/></svg>rowentallis@bellwickhomeservices.biz</li>
        <li><svg viewBox="0 0 12 12"><circle cx="6" cy="6" r="5"/></svg>www.bellwickhomeservice.biz</li>
      </ul>
    </div>
    <div class="person">
      <p class="person__name">R. Owen Tallis</p>
      <p class="person__title">President/CEO</p>
    </div>
  </section>

</main>
</body>
</html>
```